Rug Cleaning Web Design Project

We need a web design for our cleaning company. We currently have a web page but are not happy with its design. We currently offer fine rug cleaning,upholstery cleaning, and residential and commercial carpet cleanning. We also offer water damage restoration. For our rug cleaning services we offer : Enzyme treatments for pet contamination and odor removal, application of stain protection that is designed for the fine textiles used in rug construction, application of treatments designed to prevent moth damage and pads designed to be used under rugs.Our current web site is harborfreshcare.example. We are intrested in a design with similar information to the web page of Velmora Rug Cleaners INC. We would like to use the colors that are present in our logo that will be uploaded with this description. We would also like this new page to be linked to our other address loomrinsepro.example. We would like the deign to be visually attractive but not "too busy".
Updates

Please include pictures of rugs, or people washing rugs if possible. We do not offer maid type cleaning services. We would not be interested in designs including pictures depicting that type service. Thanks for your hard work on this project.

Dana Whitlow

Industry/Entity Type

Residential

Requirements
Must have
• This page must be viewable on smart phones and tablets.

```html
<!DOCTYPE html>
<html lang="en">
<head>
<meta charset="utf-8">
<meta name="viewport" content="width=1200">
<title>Loom Rinse Pro – Harborfresh Care, LLC</title>
<link rel="stylesheet" href="https://fonts.googleapis.com/css2?family=PT+Sans:wght@400;700&family=Roboto+Condensed:ital,wght@1,700&family=Arimo&display=swap">
<style>
:root{
  --page-light:#e2e1dc;
  --page-dark:#9c9b95;
  --top-bar:#7a7a7a;
  --nav-top:#1b7acb;
  --nav-mid:#0b4d86;
  --nav-bottom:#062b4d;
  --nav-active:#050d16;
  --nav-divider:#03223d;
  --brand-blue:#1565b5;
  --ink:#0b0b0b;
  --heading:#0e2741;
  --body-text:#4a4a4a;
  --panel:#ffffff;
  --heading-bar:#ececec;
  --icon:#8a8a8a;
  --footer-link:#0a1650;
  --hero-light:#c5bab2;
  --hero-dark:#8c8079;
}
*{margin:0;padding:0;box-sizing:border-box}
html,body{width:1200px;height:844px;overflow:hidden}
body{
  position:relative;
  background:radial-gradient(ellipse 700px 420px at 600px 330px,var(--page-light),#cfcec8 60%,var(--page-dark) 140%);
  font-family:"Arimo",Arial,sans-serif;
}
.top-bar{position:absolute;left:0;top:0;width:1200px;height:7px;background:var(--top-bar)}

.brand{position:absolute;left:126px;top:40px;display:flex;align-items:center;gap:14px}
.brand-dot{width:60px;height:60px;border-radius:50%;background:var(--brand-blue)}
.brand-name{font-family:"PT Sans",sans-serif;font-weight:700;font-size:40px;color:#222;letter-spacing:-0.5px}

.emergency{position:absolute;left:878px;top:56px;font-family:"Roboto Condensed",sans-serif;font-style:italic;font-weight:700;color:var(--ink);line-height:1}
.emergency .line1{font-size:25px}
.emergency .hours{font-size:32px;color:var(--brand-blue)}
.emergency .line2{display:block;font-size:31px;text-align:right;margin-right:8px}

.main-nav{position:absolute;left:114px;top:157px;width:972px;height:60px;display:flex;
  background:linear-gradient(var(--nav-top),var(--nav-mid) 55%,var(--nav-bottom));
  border-radius:16px 16px 0 0}
.main-nav a{display:flex;align-items:center;justify-content:center;height:100%;color:#fff;text-decoration:none;
  font-family:"PT Sans",sans-serif;font-size:17px;border-left:1px solid var(--nav-divider);padding-top:8px}
.main-nav a:first-child{border-left:0;border-radius:16px 0 0 0}
.main-nav a.is-active{background:linear-gradient(#1a2a3a,var(--nav-active))}

.hero{position:absolute;left:114px;top:217px;width:972px;height:294px;
  background:linear-gradient(100deg,var(--hero-light),#b4a8a0 55%,var(--hero-dark))}
.hero-title{position:absolute;left:58px;top:88px;font-family:"Roboto Condensed",sans-serif;font-style:italic;font-weight:700;font-size:46px;color:var(--ink);letter-spacing:-0.5px}
.hero-brand{position:absolute;left:208px;top:150px;display:flex;align-items:center;gap:8px}
.hero-brand .brand-dot{width:38px;height:38px}
.hero-brand .brand-name{font-size:26px}

.content-shape{position:absolute;left:114px;top:511px}
.column{position:absolute;top:511px}
.col-welcome{left:114px;width:309px}
.col-services{left:423px;width:354px;height:211px;background:var(--panel);box-shadow:0 0 14px rgba(0,0,0,.22)}
.col-contact{left:777px;width:309px}
.section-title{height:30px;margin:10px 10px 0;background:linear-gradient(var(--heading-bar),#e2e2e2);
  font-family:"PT Sans",sans-serif;font-weight:700;font-size:17px;color:var(--heading);padding:4px 18px}
.col-services .section-title{margin:10px 16px 0 12px}
.col-contact .section-title{margin-left:10px;margin-right:15px}
.welcome-text{margin:15px 20px 0 19px;font-size:10.6px;line-height:12px;color:var(--body-text)}
.welcome-text p+p{margin-top:12px}

.service-lists{display:flex;margin:17px 0 0 28px}
.service-list{list-style:none;width:170px}
.service-list li{display:flex;align-items:center;gap:6px;font-size:10.6px;color:var(--body-text);height:18px}
.service-list svg{flex:none}

.contact-list{list-style:none;margin:27px 0 0 28px}
.contact-list li{display:flex;gap:17px;font-size:10.6px;line-height:12px;color:var(--body-text)}
.contact-list li+li{margin-top:12px}
.contact-list .phone{font-weight:700;font-size:12px;color:#555;align-items:center}
.contact-list svg{flex:none}

.footer-links{position:absolute;left:0;top:771px;width:1200px;text-align:center;font-size:10.5px;color:var(--footer-link)}
.footer-links a{color:var(--footer-link);text-decoration:none}
.footer-links .sep{margin:0 13px}
</style>
</head>
<body>
<div class="top-bar"></div>

<header>
  <div class="brand"><span class="brand-dot"></span><span class="brand-name">LoomRinsePro</span></div>
  <div class="emergency"><span class="line1">Emergency </span><span class="hours">24/7</span><span class="line2">Services</span></div>
</header>

<nav class="main-nav">
  <a href="#" class="is-active" style="width:114px">Home</a>
  <a href="#" style="width:110px">About Us</a>
  <a href="#" style="width:138px">Our Services</a>
  <a href="#" style="width:194px">Request an Estimate</a>
  <a href="#" style="width:127px">Web Links</a>
  <a href="#" style="width:138px">Our Location</a>
  <a href="#" style="width:151px">Contact Us</a>
</nav>

<section class="hero" role="img" aria-label="Photo of a carpet cleaning wand gliding over beige carpet">
  <h1 class="hero-title">World Class Services</h1>
  <div class="hero-brand"><span class="brand-dot"></span><span class="brand-name">LoomRinsePro</span></div>
</section>

<svg class="content-shape" width="972" height="240" viewBox="0 0 972 240" aria-hidden="true">
  <path d="M0 0H972V188Q972 201 955 202Q486 268 17 202Q0 201 0 188Z" fill="#fff"/>
</svg>

<section class="column col-welcome">
  <h2 class="section-title">Welcome to Loom Rinse Pro</h2>
  <div class="welcome-text">
    <p>Lorem ipsum dolor sit amet, consectetur adipiscing elit. Vestibulum vitae lectus at erat ornare feugiat nec eget elit. Cras augue nunc, tincidunt sit amet consectetur ut, consequat sit amet velit.</p>
    <p>Pellentesque luctus arcu nec turpis malesuada elementum. Curabitur ac turpis eget sem tempus lobortis. Maecenas ut odio vel est sodales varius. Fusce pretium diam sodales ante.</p>
  </div>
</section>

<section class="column col-services">
  <h2 class="section-title">Our Services</h2>
  <div class="service-lists">
    <ul class="service-list">
      <li><svg width="5" height="7" viewBox="0 0 5 7"><path d="M0 0L5 3.5L0 7Z" fill="#555"/></svg>Lorem ipsum dolor.</li>
      <li><svg width="5" height="7" viewBox="0 0 5 7"><path d="M0 0L5 3.5L0 7Z" fill="#555"/></svg>Vestibulum vitae.</li>
      <li><svg width="5" height="7" viewBox="0 0 5 7"><path d="M0 0L5 3.5L0 7Z" fill="#555"/></svg>Cras augue nunc.</li>
      <li><svg width="5" height="7" viewBox="0 0 5 7"><path d="M0 0L5 3.5L0 7Z" fill="#555"/></svg>Pellentesque luctus.</li>
      <li><svg width="5" height="7" viewBox="0 0 5 7"><path d="M0 0L5 3.5L0 7Z" fill="#555"/></svg>Arcu nec turpis.</li>
      <li><svg width="5" height="7" viewBox="0 0 5 7"><path d="M0 0L5 3.5L0 7Z" fill="#555"/></svg>Malesuada elementum.</li>
      <li><svg width="5" height="7" viewBox="0 0 5 7"><path d="M0 0L5 3.5L0 7Z" fill="#555"/></svg>Curabitur ac turpis eget.</li>
      <li><svg width="5" height="7" viewBox="0 0 5 7"><path d="M0 0L5 3.5L0 7Z" fill="#555"/></svg>Sem tempuslobortis.</li>
    </ul>
    <ul class="service-list">
      <li><svg width="5" height="7" viewBox="0 0 5 7"><path d="M0 0L5 3.5L0 7Z" fill="#555"/></svg>Lorem ipsum dolor.</li>
      <li><svg width="5" height="7" viewBox="0 0 5 7"><path d="M0 0L5 3.5L0 7Z" fill="#555"/></svg>Vestibulum vitae.</li>
      <li><svg width="5" height="7" viewBox="0 0 5 7"><path d="M0 0L5 3.5L0 7Z" fill="#555"/></svg>Cras augue nunc.</li>
      <li><svg width="5" height="7" viewBox="0 0 5 7"><path d="M0 0L5 3.5L0 7Z" fill="#555"/></svg>Pellentesque luctus.</li>
      <li><svg width="5" height="7" viewBox="0 0 5 7"><path d="M0 0L5 3.5L0 7Z" fill="#555"/></svg>Arcu nec turpis.</li>
      <li><svg width="5" height="7" viewBox="0 0 5 7"><path d="M0 0L5 3.5L0 7Z" fill="#555"/></svg>Malesuada elementum.</li>
      <li><svg width="5" height="7" viewBox="0 0 5 7"><path d="M0 0L5 3.5L0 7Z" fill="#555"/></svg>Curabitur ac turpis eget.</li>
      <li><svg width="5" height="7" viewBox="0 0 5 7"><path d="M0 0L5 3.5L0 7Z" fill="#555"/></svg>Sem tempuslobortis.</li>
    </ul>
  </div>
</section>

<section class="column col-contact">
  <h2 class="section-title">Contact Us</h2>
  <ul class="contact-list">
    <li><svg width="22" height="20" viewBox="0 0 22 20"><path d="M11 1L1 10H4V19H9V13H13V19H18V10H21Z" fill="var(--icon)"/></svg><span>Lorem ipsum dolor sit amet, consectetur adipiscing elit. Vestibulum vitae lectus at.</span></li>
    <li class="phone"><svg width="22" height="18" viewBox="0 0 22 18"><path d="M6 1C4 1 3 3 3 5C4 11 9 16 15 17C17 17 18 16 18 14L15 11L12 13C10 12 8 10 7 8L9 5Z" fill="var(--icon)"/></svg><span>555-014-2276</span></li>
    <li><svg width="22" height="20" viewBox="0 0 22 20"><circle cx="11" cy="10" r="7.5" fill="none" stroke="var(--icon)" stroke-width="2"/><path d="M11 5.5V10H14.5" fill="none" stroke="var(--icon)" stroke-width="1.8"/></svg><span>M-F 8:30-4:30 and<br>Saturdays 9-11:30</span></li>
  </ul>
</section>

<footer class="footer-links">
  <span>©2012 &nbsp; All Rights Reserved</span><span class="sep">|</span><a href="#">Site Map</a><span class="sep">|</span><a href="#">Privacy Policy</a><span class="sep">|</span><a href="#">Terms &amp; Conditions</a>
</footer>
</body>
</html>
```